Landing Page - Lending & Lantern

Need a singular landing page that will eventually link to podcast and direct people to my page. I need it to work with FernoTrack.

The page is geared about small business owners and linking them with high quality banker to obtain financing. It should be professional, connect to bourbon as an underlying tone. It's all about qualify and integrity.

It needs to be put in Wordpress.
I don't know the difference between coded and uncoded, I just want it done.

Target Market(s)

Business Owners and those needing help with financing. The people we're trying to help aren't rich, they are successful but need help.

Industry/Entity Type

Finance & Bourbon

Coding

Coded - Design and coding required

Number of Pages Required

1 page

Colors
0054AA
0677BA
7BADD7
CADEEF
E8F1F8
0094D4
00A9DD
6FCCEA
C7EBF8
E9F6FB

Requirements
Must have
• Link to send email
Nice to have
• Use colors and fonts in branding.

```html
<!DOCTYPE html>
<html lang="en">
<head>
<meta charset="utf-8">
<title>Lending &amp; Lantern</title>
<link href="https://fonts.googleapis.com/css2?family=Tinos:wght@400;700&display=swap" rel="stylesheet">
<style>
:root{
  --teal:#0a9d93;
  --teal-dark:#078077;
  --ink:#0f1426;
  --night:#0b0f1e;
  --hero-a:#1b2436;
  --hero-b:#30394a;
  --white:#ffffff;
  --text:#2a2a2a;
  --rule:#d8d8d8;
}
*{margin:0;padding:0;box-sizing:border-box}
html,body{width:1200px;height:3400px;overflow:hidden}
body{position:relative;font-family:"Tinos","Times New Roman",serif;color:var(--text);background:var(--white)}
.abs{position:absolute}
.center{left:0;width:1200px;text-align:center}

/* hero */
.hero{left:0;top:0;width:1200px;height:640px;background:radial-gradient(ellipse at 50% 40%,var(--hero-b),var(--hero-a) 70%)}
.nav{left:0;top:0;width:1200px;height:118px;border-bottom:1px solid rgba(255,255,255,.18)}
.nav a{position:absolute;top:48px;color:var(--white);font-size:17px;text-decoration:none;transform:translateX(-50%);white-space:nowrap}
.nav .div{position:absolute;top:0;width:1px;height:118px;background:rgba(255,255,255,.15)}
.brand-nav{left:521px;top:14px;width:162px;height:90px;display:flex;flex-direction:column;align-items:center;justify-content:center;color:var(--teal);font-size:24px;font-weight:700;line-height:28px;text-align:center;white-space:nowrap}
.welcome{top:244px;font-size:26px;color:var(--white)}
.hero-title{top:280px;font-size:46px;font-weight:700;color:var(--teal);letter-spacing:1px}
.hero-lead{top:350px;left:280px;width:640px;text-align:center;color:var(--white);font-size:14px;line-height:25px}
.btn{display:flex;align-items:center;gap:16px;justify-content:center;font-size:21px;white-space:nowrap}
.btn-hero{left:510px;top:428px;width:180px;height:47px;border:1px solid var(--white);color:var(--white)}
.vline{width:2px}

/* about */
.eyebrow{font-size:16px;letter-spacing:.5px}
.h2{font-size:33px;font-weight:700;color:var(--ink);letter-spacing:.5px;white-space:nowrap}
.about-copy{left:99px;top:858px;width:480px;font-size:19.5px;line-height:33.5px}
.about-copy p+p{margin-top:24px}
.btn-about{left:99px;top:1187px;width:182px;height:48px;border:1px solid var(--teal);color:var(--text)}
.about-brand{left:660px;top:800px;width:470px;height:330px;display:flex;align-items:center;justify-content:center;gap:20px}
.about-brand .dot{flex:none;width:56px;height:56px;border-radius:50%;background:var(--teal)}
.about-brand span{font-size:44px;font-weight:700;color:var(--ink);white-space:nowrap}

/* podcast */
.podcast{left:0;top:1360px;width:1200px;height:814px;background:linear-gradient(180deg,#142028 0%,#0f1a1f 50%,#17252b 100%)}
.card{width:290px;height:399px;top:1620px;background:var(--teal)}
.card-photo{position:absolute;left:16px;top:16px;width:307px;height:210px}
.card h3{position:absolute;left:19px;top:236px;font-size:23px;color:var(--white);white-space:nowrap}
.card p{position:absolute;left:19px;top:278px;width:225px;font-size:14px;line-height:25px;color:var(--white)}
.player{position:absolute;left:11px;top:340px;width:265px;height:42px;border-radius:21px;background:#000}

/* news */
.news-photo{top:2400px;width:471px;height:255px}
.news-date{top:2668px;font-size:15px;font-weight:700;color:var(--ink);display:flex;gap:8px;align-items:center}
.news-rule{top:2698px;width:471px;height:1px;background:var(--rule)}
.news-text{top:2712px;width:471px;font-size:15.5px;font-weight:700;line-height:25px;color:var(--ink)}

/* footer */
.footer{left:0;top:2930px;width:1200px;height:470px;background:linear-gradient(180deg,#0a0d1a,#0e1428)}
.foot-brand{left:90px;top:3075px;width:220px;height:150px;display:flex;flex-direction:column;align-items:center;justify-content:center;gap:12px}
.foot-brand .dot{width:34px;height:34px;border-radius:50%;background:var(--white)}
.foot-brand span{color:var(--white);font-size:24px;font-weight:700;white-space:nowrap}
.foot-h{top:3030px;font-size:25px;font-weight:700;color:var(--white);white-space:nowrap}
.foot-links{list-style:none;top:3085px;color:var(--white);font-size:18px;line-height:30.5px;white-space:nowrap}
.foot-links.bold{font-weight:700}
.social{top:3096px;width:44px;height:44px;border-radius:50%;background:var(--teal)}
.foot-rule{left:99px;top:3306px;width:1002px;height:1px;background:rgba(255,255,255,.4)}
.copy{top:3337px;color:var(--white);font-size:13px;font-weight:700}
</style>
</head>
<body>

<!-- hero -->
<section class="abs hero" role="img" aria-label="Looking up at glass skyscrapers, darkened"></section>
<nav class="abs nav">
  <a style="left:160px" href="#">Home</a>
  <span class="div" style="left:218px"></span>
  <a style="left:291px" href="#">About Us</a>
  <span class="div" style="left:365px"></span>
  <a style="left:428px" href="#">Podcast</a>
  <span class="div" style="left:520px"></span>
  <div class="abs brand-nav"><span>Lending &amp;</span><span>Lantern</span></div>
  <span class="div" style="left:683px"></span>
  <a style="left:735px" href="#">News</a>
  <span class="div" style="left:806px"></span>
  <a style="left:858px" href="#">Careers</a>
  <span class="div" style="left:937px"></span>
  <a style="left:1000px" href="mailto:hello@lendinglantern.com">Contact Us</a>
</nav>
<div class="abs center welcome">WELCOME TO</div>
<h1 class="abs center hero-title">LENDING AND LANTERN</h1>
<p class="abs hero-lead">Lorem ipsum dolor sit amet, consectetur adipiscing elit, sed do eiusmod tempor incididunt ut labore et dolore magna aliqua. Ut enim ad minim veniam, quis nostrud exercitation.</p>
<a class="abs btn btn-hero">Get Started
  <svg width="18" height="18" viewBox="0 0 18 18"><circle cx="9" cy="9" r="9" fill="#fff"/><path d="M5 9h7M9 5.5 12.5 9 9 12.5" stroke="#1b2436" stroke-width="2" fill="none"/></svg>
</a>
<div class="abs vline" style="left:599px;top:562px;height:78px;background:#fff"></div>

<!-- about -->
<div class="abs eyebrow" style="left:99px;top:764px">WHO WE ARE</div>
<h2 class="abs h2" style="left:99px;top:796px">ABOUT SMALL BUSINESS</h2>
<div class="abs about-copy">
  <p>Sed ut perspiciatis unde omnis iste natus error sit voluptatem accusantium doloremque laudantium, totam rem aperiam, eaque ipsa quae ab illo inventore veritatis et quasi architecto beatae vitae dicta sunt explicabo.</p>
  <p>Sed ut perspiciatis unde omnis iste natus error sit voluptatem accusantium doloremque laudantium, totam rem aperiam, eaque ipsa quae ab illo inventore veritatis et quasi architecto beatae vitae dicta sunt explicabo.</p>
</div>
<a class="abs btn btn-about">Read More
  <svg width="18" height="18" viewBox="0 0 18 18"><circle cx="9" cy="9" r="9" fill="#111"/><path d="M5 9h7M9 5.5 12.5 9 9 12.5" stroke="#fff" stroke-width="2" fill="none"/></svg>
</a>
<div class="abs about-brand"><div class="dot"></div><span>Lending &amp; Lantern</span></div>

<!-- podcast -->
<section class="abs podcast" role="img" aria-label="Dim city skyline at night with digital data lines"></section>
<div class="abs vline" style="left:599px;top:1360px;height:114px;background:#fff"></div>
<div class="abs" style="left:588px;top:1473px;width:24px;height:2px;background:#fff"></div>
<div class="abs center eyebrow" style="top:1498px;color:#fff">WHAT WE DO</div>
<h2 class="abs center h2" style="top:1530px;color:#fff">OUR PODCAST</h2>

<div class="abs card" style="left:99px">
  <div class="card-photo" role="img" aria-label="Smiling businesswoman shaking hands at a desk" style="background:linear-gradient(135deg,#c9c7c2,#8e8a84)"></div>
  <h3>Neque porro quisquam</h3>
  <p>"Sed ut perspiciatis unde omnis iste natus error sit voluptatem</p>
  <div class="player"><svg width="265" height="42" viewBox="0 0 265 42"><circle cx="22" cy="21" r="8" fill="none" stroke="#fff" stroke-width="2"/><path d="M20 17v8l6-4z" fill="#fff"/><rect x="42" y="19" width="168" height="4" rx="2" fill="#fff"/><rect x="42" y="19" width="55" height="4" rx="2" fill="#0a9d93"/><path d="M232 17h4l5-4v16l-5-4h-4z" fill="#fff"/><path d="M244 16q4 5 0 10M247 13q7 8 0 16" stroke="#fff" stroke-width="2" fill="none"/></svg></div>
</div>
<div class="abs card" style="left:438px">
  <div class="card-photo" role="img" aria-label="Two colleagues reviewing a tablet in an office" style="background:linear-gradient(135deg,#d6d2c8,#8a857b)"></div>
  <h3>Neque porro quisquam</h3>
  <p>"Sed ut perspiciatis unde omnis iste natus error sit voluptatem</p>
  <div class="player"><svg width="265" height="42" viewBox="0 0 265 42"><circle cx="22" cy="21" r="8" fill="none" stroke="#fff" stroke-width="2"/><path d="M20 17v8l6-4z" fill="#fff"/><rect x="42" y="19" width="168" height="4" rx="2" fill="#fff"/><rect x="42" y="19" width="55" height="4" rx="2" fill="#0a9d93"/><path d="M232 17h4l5-4v16l-5-4h-4z" fill="#fff"/><path d="M244 16q4 5 0 10M247 13q7 8 0 16" stroke="#fff" stroke-width="2" fill="none"/></svg></div>
</div>
<div class="abs card" style="left:777px">
  <div class="card-photo" role="img" aria-label="Woman working on a laptop holding a card" style="background:linear-gradient(135deg,#4a4f57,#c9a486)"></div>
  <h3>Neque porro quisquam</h3>
  <p>"Sed ut perspiciatis unde omnis iste natus error sit voluptatem</p>
  <div class="player"><svg width="265" height="42" viewBox="0 0 265 42"><circle cx="22" cy="21" r="8" fill="none" stroke="#fff" stroke-width="2"/><path d="M20 17v8l6-4z" fill="#fff"/><rect x="42" y="19" width="168" height="4" rx="2" fill="#fff"/><rect x="42" y="19" width="55" height="4" rx="2" fill="#0a9d93"/><path d="M232 17h4l5-4v16l-5-4h-4z" fill="#fff"/><path d="M244 16q4 5 0 10M247 13q7 8 0 16" stroke="#fff" stroke-width="2" fill="none"/></svg></div>
</div>
<div class="abs vline" style="left:599px;top:2110px;height:148px;background:var(--teal)"></div>
<div class="abs" style="left:588px;top:2257px;width:24px;height:2px;background:var(--teal)"></div>

<!-- news -->
<div class="abs center eyebrow" style="top:2282px">NEWS</div>
<h2 class="abs center h2" style="top:2313px">RECENT UPDATES</h2>

<div class="abs news-photo" style="left:98px;background:linear-gradient(135deg,#e6ddd0,#8f9a6e)" role="img" aria-label="Woman with glasses working on a laptop at home"></div>
<div class="abs news-date" style="left:98px"><svg width="16" height="16" viewBox="0 0 16 16"><rect x="1" y="3" width="14" height="12" fill="none" stroke="#0a9d93" stroke-width="1.5"/><path d="M1 7h14M5 1v4M11 1v4" stroke="#0a9d93" stroke-width="1.5"/></svg>23/09/2023</div>
<div class="abs news-rule" style="left:98px"></div>
<p class="abs news-text" style="left:98px">Nemo enim ipsam voluptatem quia voluptas sit aspernatur aut odit aut fugit, sed quia consequuntur magni dolores eos qui ratione voluptatem sequi nesciunt.</p>

<div class="abs news-photo" style="left:627px;background:linear-gradient(135deg,#3c4a55,#b9aa9a)" role="img" aria-label="Man with glasses reviewing documents with a client"></div>
<div class="abs news-date" style="left:627px"><svg width="16" height="16" viewBox="0 0 16 16"><rect x="1" y="3" width="14" height="12" fill="none" stroke="#0a9d93" stroke-width="1.5"/><path d="M1 7h14M5 1v4M11 1v4" stroke="#0a9d93" stroke-width="1.5"/></svg>23/09/2023</div>
<div class="abs news-rule" style="left:627px"></div>
<p class="abs news-text" style="left:627px">Nemo enim ipsam voluptatem quia voluptas sit aspernatur aut odit aut fugit, sed quia consequuntur magni dolores eos qui ratione voluptatem sequi nesciunt.</p>

<div class="abs vline" style="left:599px;top:2858px;height:72px;background:#111"></div>

<!-- footer -->
<footer class="abs footer"></footer>
<div class="abs foot-brand"><div class="dot"></div><span>Lending &amp; Lantern</span></div>
<h4 class="abs foot-h" style="left:400px">QUICK LINKS</h4>
<ul class="abs foot-links bold" style="left:402px">
  <li>Home</li><li>About Us</li><li>Podcast</li><li>News</li><li>Careers</li><li>Conatct Us</li>
</ul>
<h4 class="abs foot-h" style="left:660px">HELP LINKS</h4>
<ul class="abs foot-links" style="left:661px">
  <li>Terms &amp; Conditions</li><li>Privacy Policy</li><li>About Us</li><li>Support</li>
</ul>
<h4 class="abs foot-h" style="left:905px">FOLLOW US</h4>
<div class="abs social" style="left:911px"></div>
<div class="abs social" style="left:972px"></div>
<div class="abs foot-rule"></div>
<div class="abs center copy">© copyrights 2023 © Lending And Lantern |&nbsp; All Rights Reserved</div>

</body>
</html>
```